Company or website name
- FreedFromQuietHarmToday.com
- Links to the website
- Nora Joyce Palmer, mental health professional,new book,"Hushed Walls, Yet Open Doors Await" - Brought to the point of the unspoken-helping people get out and stay out of emotionally abusive relationships-www.FreedFromQuietHarmToday.com
- Other Facts

```html
<!DOCTYPE html>
<html lang="en">
<head>
<meta charset="utf-8">
<title>FreedFromQuietHarmToday.com</title>
<link rel="stylesheet" href="https://fonts.googleapis.com/css2?family=Crimson+Pro:wght@400&display=swap">
<style>
  :root {
    --night: #000000;
    --ink-white: #ffffff;
    --photo-light: #9ea2a7;
    --photo-mid: #55595e;
    --serif: "Crimson Pro", "Palatino Linotype", Palatino, serif;
  }
  html, body {
    margin: 0;
    padding: 0;
    overflow: hidden;
    background: var(--night);
  }
  .banner {
    position: relative;
    width: 1200px;
    height: 253px;
    background: var(--night);
    overflow: hidden;
  }
  .banner__photo {
    position: absolute;
    left: 0;
    top: 0;
    width: 270px;
    height: 253px;
    background: linear-gradient(90deg, var(--photo-light) 0%, var(--photo-mid) 50%, var(--night) 100%);
  }
  .banner__title {
    position: absolute;
    left: 0;
    top: 0;
  }
  .banner__title text {
    font-family: var(--serif);
    font-size: 66px;
    fill: var(--ink-white);
  }
  .signature {
    position: absolute;
    left: 940px;
    top: 192px;
    width: 220px;
    font-family: var(--serif);
    font-size: 16px;
    line-height: 1;
    letter-spacing: 3px;
    color: var(--ink-white);
    text-transform: uppercase;
    text-align: center;
  }
  .signature__row {
    display: flex;
    align-items: center;
    justify-content: center;
    gap: 10px;
  }
  .signature__dot {
    width: 26px;
    height: 26px;
    border: 1.5px solid var(--ink-white);
    border-radius: 50%;
  }
  .signature__last {
    display: block;
    margin-top: 4px;
  }
</style>
</head>
<body>
  <main class="banner">
    <div class="banner__photo" role="img" aria-label="Black and white close-up photograph of an eye with a falling tear"></div>

    <svg class="banner__title" width="1200" height="253" viewBox="0 0 1200 253">
      <text x="296" y="145" textLength="856" lengthAdjust="spacingAndGlyphs">FreedFromQuietHarmToday.com</text>
    </svg>

    <div class="signature">
      <div class="signature__row">
        <span class="signature__first">Nora</span>
        <span class="signature__dot"></span>
        <span class="signature__middle">Joyce</span>
      </div>
      <span class="signature__last">Palmer</span>
    </div>
  </main>
</body>
</html>
```